Calendar Design Project: 2025 with Specific Edits

This is a straightforward project where your creativity can shine!
Simply take the existing 2024 calendar and adapt it for 2025 by incorporating the new photos I've attached.
Please keep the overall concept of the 2024 calendar intact—your focus will be on enhancing it with fresh visuals.

I can't wait to see your amazing designs!
I am looking for a talented graphic designer to create a new 2025 calendar with specific adjustments.
Pictures attached.
Requirements:
Calendar Size: 52cm x 34cm
March Folder:
Adjust the image named "attached - DJI-0025" to make the circular road darker to match the rest of the design.
May Folder:
Modify the circled area in the May image to ensure it looks consistent with the other road (reference file: "attached - After").
November Folder:
Clear out the circled area in the November image (reference file: "attached - After1").
Please let me know if you have any questions or need further clarification.
I added to my breif a design i made last year for same client.
2025, calendar should be vertical and not horizontal. and some of the photos attache are "Before" and "After" please include together inside each month of the calendar.
Thank you!
Feel free to adjust any details as necessary!

Hello talented designers!

I’m excited to share that this is my 14th project on the ArtHarbor platform, and I’ve been fortunate to have successful collaborations in the past. I'm looking forward to creating a new 2025 calendar with your help, and I believe that with your creativity and skills, we can make this project a success as well!

I hope to establish a long-term relationship with a talented team like yours. As an added incentive, I will be offering a bonus for the winner, and I may select more than one winner, so everyone has a chance to shine!

Let’s make something amazing together!

Best
Update:
cancel or before, only place the After picture

Requirements
Must have
• Project Overview Objective: Create a 2025 calendar using the provided images, maintaining the design concept from the 2024 calendar but enhancing it with new visuals. Format: Vertical layout (52cm x 34cm).

```html
<!DOCTYPE html>
<html lang="en">
<head>
<meta charset="utf-8">
<title>2025 Wall Calendar – March</title>
<link href="https://fonts.googleapis.com/css2?family=Montserrat:wght@600;800&family=Arimo:wght@400;700&family=Didact+Gothic&display=swap" rel="stylesheet">
<style>
  :root{
    --backdrop:#000000;
    --paper:#ffffff;
    --brand-green:#3a9e4c;
    --band-green:#4caf5a;
    --ink:#111111;
    --sunday:#a3173c;
    --row-grey:#efefef;
    --frame-line:#e4e4e4;
    --photo-sky:#c9d6de;
    --photo-city:#8a7360;
    --photo-ground:#a5633f;
  }
  html,body{margin:0;padding:0;width:1200px;height:1200px;overflow:hidden;background:var(--backdrop);}
  .calendar-canvas{display:block;width:1200px;height:1200px;}
  .weekday,.day{font-family:"Arimo",Arial,sans-serif;fill:var(--ink);}
  .sun{fill:var(--sunday);}
  .month-title{font-family:"Montserrat",Arial,sans-serif;font-weight:800;fill:#fff;}
  .band-word{font-family:"Arimo",Arial,sans-serif;font-weight:400;fill:#fff;}
  .band-year{font-family:"Arimo",Arial,sans-serif;font-weight:700;fill:#fff;}
  .company-name{font-family:"Montserrat",Arial,sans-serif;font-weight:600;fill:var(--ink);}
  .contact-line{font-family:"Didact Gothic",Arial,sans-serif;fill:var(--ink);}
</style>
</head>
<body>
<svg class="calendar-canvas" viewBox="0 0 1932 1932" xmlns="http://www.w3.org/2000/svg">
  <defs>
    <linearGradient id="photoTone" x1="0" y1="0" x2="0" y2="1">
      <stop offset="0" stop-color="var(--photo-sky)"/>
      <stop offset="0.12" stop-color="var(--photo-city)"/>
      <stop offset="0.65" stop-color="#6f6a66"/>
      <stop offset="1" stop-color="var(--photo-ground)"/>
    </linearGradient>
    <linearGradient id="gridFade" x1="0" y1="0" x2="0" y2="1">
      <stop offset="0" stop-color="#ffffff"/>
      <stop offset="1" stop-color="#e6e6e6"/>
    </linearGradient>
    <radialGradient id="dropShade" cx="0.5" cy="0" r="0.5">
      <stop offset="0" stop-color="#000" stop-opacity="0.35"/>
      <stop offset="1" stop-color="#000" stop-opacity="0"/>
    </radialGradient>
  </defs>

  <!-- page -->
  <rect class="page" x="386" y="79" width="1160" height="1774" fill="var(--paper)"/>

  <!-- hero photo frame -->
  <polygon class="photo-frame" points="420,115 1298,115 1432,228 1432,1016 562,1016 420,890" fill="none" stroke="var(--frame-line)" stroke-width="2"/>
  <polygon class="hero-photo" role="img" aria-label="Aerial photo of a newly built elevated concrete flyover road crossing a dense town of rooftops and a small river"
    points="428,118 1297,118 1420,240 1420,1000 565,1000 428,836" fill="url(#photoTone)"/>

  <!-- green title band -->
  <polygon class="title-band" points="1298,145 1508,318 1508,1042 1298,855" fill="var(--band-green)"/>
  <g class="band-title">
    <text class="band-word" transform="translate(1410,850) rotate(-90)" font-size="74" textLength="170" lengthAdjust="spacingAndGlyphs">CALE</text>
    <text class="band-word" transform="translate(1467,860) rotate(-90)" font-size="74" textLength="185" lengthAdjust="spacingAndGlyphs">NDAR</text>
    <text class="band-year" transform="translate(1465,645) rotate(-90)" font-size="156" textLength="315" lengthAdjust="spacingAndGlyphs">2025</text>
  </g>

  <!-- March main grid -->
  <g class="month-main">
    <ellipse cx="772" cy="1656" rx="320" ry="12" fill="url(#dropShade)"/>
    <rect x="445" y="1158" width="654" height="492" fill="url(#gridFade)"/>
    <rect x="445" y="1158" width="654" height="62" fill="var(--row-grey)"/>
    <path d="M444,1155 V1078 Q444,1052 470,1052 H1073 Q1099,1052 1099,1078 V1155 Z" fill="var(--brand-green)"/>
    <text class="month-title" x="772" y="1133" font-size="50" text-anchor="middle">MARCH</text>
    <g font-size="38" text-anchor="middle">
      <text class="weekday sun" x="491" y="1202">Sun</text>
      <text class="weekday" x="585" y="1202">Mon</text>
      <text class="weekday" x="678" y="1202">Tue</text>
      <text class="weekday" x="772" y="1202">Wed</text>
      <text class="weekday" x="866" y="1202">Thu</text>
      <text class="weekday" x="958" y="1202">Fri</text>
      <text class="weekday" x="1052" y="1202">Sat</text>
    </g>
    <g font-size="50" text-anchor="middle">
      <text class="day" x="1052" y="1275">1</text>
      <text class="day sun" x="491" y="1346">2</text><text class="day" x="585" y="1346">3</text><text class="day" x="678" y="1346">4</text><text class="day" x="772" y="1346">5</text><text class="day" x="866" y="1346">6</text><text class="day" x="958" y="1346">7</text><text class="day" x="1052" y="1346">8</text>
      <text class="day sun" x="491" y="1417">9</text><text class="day" x="585" y="1417">10</text><text class="day" x="678" y="1417">11</text><text class="day" x="772" y="1417">12</text><text class="day" x="866" y="1417">13</text><text class="day" x="958" y="1417">14</text><text class="day" x="1052" y="1417">15</text>
      <text class="day sun" x="491" y="1489">16</text><text class="day" x="585" y="1489">17</text><text class="day" x="678" y="1489">18</text><text class="day" x="772" y="1489">19</text><text class="day" x="866" y="1489">20</text><text class="day" x="958" y="1489">21</text><text class="day" x="1052" y="1489">22</text>
      <text class="day sun" x="491" y="1561">23</text><text class="day" x="585" y="1561">24</text><text class="day" x="678" y="1561">25</text><text class="day" x="772" y="1561">26</text><text class="day" x="866" y="1561">27</text><text class="day" x="958" y="1561">28</text><text class="day" x="1052" y="1561">29</text>
      <text class="day sun" x="491" y="1633">30</text><text class="day" x="585" y="1633">31</text>
    </g>
  </g>

  <!-- February mini grid -->
  <g class="month-mini">
    <ellipse cx="1308" cy="1344" rx="150" ry="7" fill="url(#dropShade)"/>
    <rect x="1150" y="1103" width="316" height="236" fill="url(#gridFade)"/>
    <rect x="1150" y="1103" width="316" height="30" fill="var(--row-grey)"/>
    <path d="M1150,1100 V1062 Q1150,1052 1160,1052 H1456 Q1466,1052 1466,1062 V1100 Z" fill="var(--brand-green)"/>
    <text class="month-title" x="1308" y="1090" font-size="22" text-anchor="middle">FEBRUARY</text>
    <g font-size="19" text-anchor="middle">
      <text class="weekday sun" x="1173" y="1125">Sun</text><text class="weekday" x="1218" y="1125">Mon</text><text class="weekday" x="1263" y="1125">Tue</text><text class="weekday" x="1308" y="1125">Wed</text><text class="weekday" x="1353" y="1125">Thu</text><text class="weekday" x="1398" y="1125">Fri</text><text class="weekday" x="1443" y="1125">Sat</text>
    </g>
    <g font-size="22" text-anchor="middle">
      <text class="day" x="1443" y="1160">1</text>
      <text class="day sun" x="1173" y="1194">2</text><text class="day" x="1218" y="1194">3</text><text class="day" x="1263" y="1194">4</text><text class="day" x="1308" y="1194">5</text><text class="day" x="1353" y="1194">6</text><text class="day" x="1398" y="1194">7</text><text class="day" x="1443" y="1194">8</text>
      <text class="day sun" x="1173" y="1228">9</text><text class="day" x="1218" y="1228">10</text><text class="day" x="1263" y="1228">11</text><text class="day" x="1308" y="1228">12</text><text class="day" x="1353" y="1228">13</text><text class="day" x="1398" y="1228">14</text><text class="day" x="1443" y="1228">15</text>
      <text class="day sun" x="1173" y="1263">16</text><text class="day" x="1218" y="1263">17</text><text class="day" x="1263" y="1263">18</text><text class="day" x="1308" y="1263">19</text><text class="day" x="1353" y="1263">20</text><text class="day" x="1398" y="1263">21</text><text class="day" x="1443" y="1263">22</text>
      <text class="day sun" x="1173" y="1297">23</text><text class="day" x="1218" y="1297">24</text><text class="day" x="1263" y="1297">25</text><text class="day" x="1308" y="1297">26</text><text class="day" x="1353" y="1297">27</text><text class="day" x="1398" y="1297">28</text><text class="day" x="1443" y="1297">29</text>
      <text class="day sun" x="1173" y="1332">30</text><text class="day" x="1218" y="1332">31</text>
    </g>
  </g>

  <!-- April mini grid -->
  <g class="month-mini" transform="translate(0,311)">
    <ellipse cx="1308" cy="1344" rx="150" ry="7" fill="url(#dropShade)"/>
    <rect x="1150" y="1103" width="316" height="236" fill="url(#gridFade)"/>
    <rect x="1150" y="1103" width="316" height="30" fill="var(--row-grey)"/>
    <path d="M1150,1100 V1062 Q1150,1052 1160,1052 H1456 Q1466,1052 1466,1062 V1100 Z" fill="var(--brand-green)"/>
    <text class="month-title" x="1308" y="1090" font-size="22" text-anchor="middle">APRIL</text>
    <g font-size="19" text-anchor="middle">
      <text class="weekday sun" x="1173" y="1125">Sun</text><text class="weekday" x="1218" y="1125">Mon</text><text class="weekday" x="1263" y="1125">Tue</text><text class="weekday" x="1308" y="1125">Wed</text><text class="weekday" x="1353" y="1125">Thu</text><text class="weekday" x="1398" y="1125">Fri</text><text class="weekday" x="1443" y="1125">Sat</text>
    </g>
    <g font-size="22" text-anchor="middle">
      <text class="day" x="1443" y="1160">1</text>
      <text class="day sun" x="1173" y="1194">2</text><text class="day" x="1218" y="1194">3</text><text class="day" x="1263" y="1194">4</text><text class="day" x="1308" y="1194">5</text><text class="day" x="1353" y="1194">6</text><text class="day" x="1398" y="1194">7</text><text class="day" x="1443" y="1194">8</text>
      <text class="day sun" x="1173" y="1228">9</text><text class="day" x="1218" y="1228">10</text><text class="day" x="1263" y="1228">11</text><text class="day" x="1308" y="1228">12</text><text class="day" x="1353" y="1228">13</text><text class="day" x="1398" y="1228">14</text><text class="day" x="1443" y="1228">15</text>
      <text class="day sun" x="1173" y="1263">16</text><text class="day" x="1218" y="1263">17</text><text class="day" x="1263" y="1263">18</text><text class="day" x="1308" y="1263">19</text><text class="day" x="1353" y="1263">20</text><text class="day" x="1398" y="1263">21</text><text class="day" x="1443" y="1263">22</text>
      <text class="day sun" x="1173" y="1297">23</text><text class="day" x="1218" y="1297">24</text><text class="day" x="1263" y="1297">25</text><text class="day" x="1308" y="1297">26</text><text class="day" x="1353" y="1297">27</text><text class="day" x="1398" y="1297">28</text><text class="day" x="1443" y="1297">29</text>
      <text class="day sun" x="1173" y="1332">30</text><text class="day" x="1218" y="1332">31</text>
    </g>
  </g>

  <!-- company name -->
  <g class="company">
    <rect x="466" y="1730" width="26" height="26" fill="var(--brand-green)"/>
    <text class="company-name" x="504" y="1754" font-size="36">Kestrel</text>
    <text class="company-name" x="466" y="1800" font-size="26">Construction Ltd</text>
  </g>

  <!-- contact details -->
  <g class="contacts">
    <path d="M775,1741 a8,8 0 0 1 16,0 c0,7 -8,15 -8,15 s-8,-8 -8,-15 z" fill="var(--brand-green)"/>
    <circle cx="783" cy="1741" r="3" fill="#fff"/>
    <text class="contact-line" x="796" y="1756" font-size="23">7A, Harlow Lane, Off Marsh Crescent, Eastfield</text>

    <path d="M774,1775 q0,12 12,15 l3,-4 -4,-3 -3,2 q-4,-2 -5,-6 l2,-2 -3,-4 z" fill="var(--brand-green)"/>
    <text class="contact-line" x="794" y="1788" font-size="23">2348105552741  |</text>
    <rect x="958" y="1776" width="14" height="11" fill="none" stroke="var(--brand-green)" stroke-width="2"/>
    <path d="M958,1776 l7,6 7,-6" fill="none" stroke="var(--brand-green)" stroke-width="2"/>
    <text class="contact-line" x="977" y="1788" font-size="23">info@kestrelbuild.com  |</text>
    <circle cx="1217" cy="1781" r="7" fill="none" stroke="var(--brand-green)" stroke-width="2"/>
    <path d="M1210,1781 h14 M1217,1774 v14" stroke="var(--brand-green)" stroke-width="1.5"/>
    <text class="contact-line" x="1232" y="1788" font-size="23">www.kestrelbuild.com</text>
  </g>
</svg>
</body>
</html>
```